NEW FACEBOOK AD CREATIVES FOR MARKETING AGENCY

We need one single static image AND a Carousel Ad Design With 5 Cards Total in it.

We advertise a SaaS Product that teaches businesses how to use incentive based marketing to get more sales and leads.

Using our service businesses can give away smart devices like smartwatches, earpods, mp4 players, tablets, etc. as a gift bonus along with their product or service as an added value benefit to help them create more attractive offers and to get more sales.

I have attached two designs that get me my best results on facebook ads so far so I want to create something very similar with a different look and showcasing 3-4 of the items I have attached images for.

CONTENT & INSTRUCTIONS:
MAIN TEXT: TRIPLE YOUR SALES OFFERING FREE SMART DEVICES AS A BONUS FOR BUYING YOUR PRODUCT OR SERVICE

Target Market(s)

ENTREPRENEURS, INVESTORS, BUSINESS OWNERS, MEDIA AGENCIES, BROKERAGES

Industry/Entity Type

marketing gifting

Requirements
Must have
• must match color scheme of website www.brightlanepromoworks.biz as this is where they will be redirected to when they click.
Nice to have
• the ads must be 1080x1080 Static newsfeed ad and carousel ads

```html
<!DOCTYPE html>
<html lang="en">
<head>
<meta charset="utf-8">
<title>Triple Your Sales – Ad Set</title>
<link href="https://fonts.googleapis.com/css2?family=Anton&family=Roboto:wght@500;700&display=swap" rel="stylesheet">
<style>
  :root {
    --navy: #1e1c6c;
    --orange: #ff7f00;
    --ring-blue: #1179c7;
    --cta: #ff3d00;
    --white: #ffffff;
    --paper: #ffffff;
    --rule: #8d8fb8;
    --brand-blue: #1a73c1;
  }
  * { box-sizing: border-box; margin: 0; padding: 0; }
  html, body { width: 869px; height: 1200px; overflow: hidden; background: var(--paper); }
  body { position: relative; font-family: "Anton", "Impact", sans-serif; }

  .ad-frame { position: absolute; box-shadow: 0 4px 18px rgba(0,0,0,0.12); overflow: hidden; }
  .ad-frame--main { left: 77px; top: 55px; width: 716px; height: 716px; }
  .ad-frame--left { left: 77px; top: 819px; width: 340px; height: 340px; }
  .ad-frame--right { left: 452px; top: 819px; width: 340px; height: 340px; }

  .ad { position: absolute; left: 0; top: 0; width: 716px; height: 716px; background: var(--navy); overflow: hidden; transform-origin: 0 0; }
  .ad--small { transform: scale(0.4749); }

  .headline { position: absolute; left: 0; width: 100%; text-align: center; line-height: 1; color: var(--white); text-transform: uppercase; }
  .headline--kicker { top: 60px; font-size: 26px; text-transform: none; }
  .headline--kicker span { text-transform: uppercase; }
  .kicker-rule { position: absolute; top: 73px; height: 2px; width: 79px; background: var(--rule); }
  .kicker-rule--left { left: 214px; }
  .kicker-rule--right { left: 422px; }
  .headline--hero { top: 82px; font-size: 66px; color: var(--orange); }
  .headline--offer { top: 147px; font-size: 38px; }
  .headline--bonus { top: 192px; font-size: 25px; }
  .headline--product { top: 225px; font-size: 25px; }

  .ring { position: absolute; left: 84px; top: 299px; width: 548px; height: 548px; border-radius: 50%; background: var(--ring-blue); }
  .ring-inner { position: absolute; left: 120px; top: 335px; width: 476px; height: 476px; border-radius: 50%; background: var(--white); }

  .product-photo { position: absolute; left: 173px; top: 371px; width: 358px; height: 247px; border-radius: 40px 40px 24px 24px;
    background: radial-gradient(ellipse at 55% 35%, #4a4a4f 0%, #2b2b2e 45%, #d9d9db 75%, #f2f2f2 100%); }
  .ticket-photo { position: absolute; left: 85px; top: 277px; width: 530px; height: 360px; border-radius: 14px;
    background: linear-gradient(100deg, #f59a2c 0%, #e8418f 35%, #f6c235 62%, #1aa7b5 100%); transform: rotate(-4deg); }

  .footer-band { position: absolute; left: 0; top: 639px; width: 100%; height: 77px; background: var(--white); }
  .brand { position: absolute; left: 26px; top: 22px; display: flex; align-items: center; gap: 10px;
    font-family: "Roboto", Arial, sans-serif; font-weight: 700; font-size: 21px; color: var(--brand-blue); letter-spacing: 0.5px; }
  .brand-dot { width: 26px; height: 26px; border-radius: 50%; background: var(--brand-blue); }
  .cta { position: absolute; left: 376px; top: 21px; width: 305px; height: 42px; border-radius: 6px; background: var(--cta);
    color: var(--white); font-family: "Roboto", Arial, sans-serif; font-weight: 500; font-size: 21px;
    display: flex; align-items: center; justify-content: center; letter-spacing: 0.3px; }
  .cta--centered { left: 206px; width: 304px; }

  .decor { position: absolute; left: 0; top: 0; width: 716px; height: 716px; pointer-events: none; }
</style>
</head>
<body>

<!-- Main static ad -->
<div class="ad-frame ad-frame--main">
  <div class="ad">
    <div class="ring"></div>
    <div class="ring-inner"></div>
    <div class="product-photo" role="img" aria-label="Bluetooth speaker, two smartwatches and wireless earbuds in their case"></div>

    <div class="kicker-rule kicker-rule--left"></div>
    <div class="kicker-rule kicker-rule--right"></div>
    <div class="headline headline--kicker"><span>TRIPLE</span> to</div>
    <div class="headline headline--hero">3X YOUR SALES</div>
    <div class="headline headline--offer">Offering free smart devices</div>
    <div class="headline headline--bonus">As a bonus for buying your</div>
    <div class="headline headline--product">Product or service</div>

    <svg class="decor" viewBox="0 0 716 716" aria-hidden="true">
      <g fill="#ffffff">
        <circle cx="627" cy="27" r="2.5"/><circle cx="637" cy="27" r="2.5"/><circle cx="647" cy="27" r="2.5"/><circle cx="657" cy="27" r="2.5"/><circle cx="667" cy="27" r="2.5"/><circle cx="677" cy="27" r="2.5"/><circle cx="687" cy="27" r="2.5"/>
        <circle cx="624" cy="38" r="2.5"/><circle cx="634" cy="38" r="2.5"/><circle cx="644" cy="38" r="2.5"/><circle cx="654" cy="38" r="2.5"/><circle cx="664" cy="38" r="2.5"/><circle cx="674" cy="38" r="2.5"/>
      </g>
      <g fill="#ff7f00">
        <circle cx="39" cy="57" r="2.3"/><circle cx="39" cy="69" r="2.3"/><circle cx="39" cy="81" r="2.3"/><circle cx="39" cy="93" r="2.3"/><circle cx="39" cy="105" r="2.3"/>
        <circle cx="50" cy="66" r="2.3"/><circle cx="50" cy="78" r="2.3"/><circle cx="50" cy="90" r="2.3"/><circle cx="50" cy="102" r="2.3"/><circle cx="50" cy="119" r="2.3"/>
      </g>
      <g stroke-width="3" stroke-linecap="round">
        <path d="M613 262v16M605 270h16" stroke="#ff7f00"/>
        <path d="M79 319v16M71 327h16" stroke="#ffffff"/>
        <path d="M662 544v16M654 552h16" stroke="#ffffff"/>
        <path d="M142 579v16M134 587h16" stroke="#ff7f00"/>
      </g>
    </svg>

    <div class="footer-band">
      <div class="brand"><span class="brand-dot"></span>BRIGHTLANE PROMOWORKS</div>
      <div class="cta">START A RISK FREE TRIAL</div>
    </div>
  </div>
</div>

<!-- Carousel card: travel vouchers -->
<div class="ad-frame ad-frame--left">
  <div class="ad ad--small">
    <div class="ring"></div>
    <div class="ticket-photo" role="img" aria-label="Fanned travel, dining, fitness and hotel gift voucher cards"></div>

    <div class="kicker-rule kicker-rule--left"></div>
    <div class="kicker-rule kicker-rule--right"></div>
    <div class="headline headline--kicker"><span>TRIPLE</span> to</div>
    <div class="headline headline--hero">3X YOUR SALES</div>
    <div class="headline headline--offer">Offering free smart devices</div>
    <div class="headline headline--bonus">As a bonus for buying your</div>
    <div class="headline headline--product">Product or service</div>

    <svg class="decor" viewBox="0 0 716 716" aria-hidden="true">
      <g fill="#ffffff">
        <circle cx="627" cy="27" r="2.5"/><circle cx="637" cy="27" r="2.5"/><circle cx="647" cy="27" r="2.5"/><circle cx="657" cy="27" r="2.5"/><circle cx="667" cy="27" r="2.5"/><circle cx="677" cy="27" r="2.5"/><circle cx="687" cy="27" r="2.5"/>
        <circle cx="624" cy="38" r="2.5"/><circle cx="634" cy="38" r="2.5"/><circle cx="644" cy="38" r="2.5"/><circle cx="654" cy="38" r="2.5"/><circle cx="664" cy="38" r="2.5"/><circle cx="674" cy="38" r="2.5"/>
      </g>
      <g fill="#ff7f00">
        <circle cx="55" cy="470" r="2.3"/><circle cx="55" cy="482" r="2.3"/><circle cx="55" cy="494" r="2.3"/><circle cx="55" cy="506" r="2.3"/><circle cx="55" cy="518" r="2.3"/>
        <circle cx="65" cy="476" r="2.3"/><circle cx="65" cy="488" r="2.3"/><circle cx="65" cy="500" r="2.3"/><circle cx="65" cy="512" r="2.3"/>
      </g>
      <g stroke-width="3" stroke-linecap="round">
        <path d="M50 76v16M42 84h16" stroke="#ffffff"/>
        <path d="M585 235v12M579 241h12" stroke="#ff7f00"/>
        <path d="M106 274v12M100 280h12" stroke="#ff7f00"/>
        <path d="M661 530v16M653 538h16" stroke="#ffffff"/>
      </g>
    </svg>

    <div class="footer-band">
      <div class="cta cta--centered">START A RISK FREE TRIAL</div>
    </div>
  </div>
</div>

<!-- Carousel card: smart devices -->
<div class="ad-frame ad-frame--right">
  <div class="ad ad--small">
    <div class="ring"></div>
    <div class="ring-inner"></div>
    <div class="product-photo" role="img" aria-label="Bluetooth speaker, two smartwatches and wireless earbuds in their case"></div>

    <div class="kicker-rule kicker-rule--left"></div>
    <div class="kicker-rule kicker-rule--right"></div>
    <div class="headline headline--kicker"><span>TRIPLE</span> to</div>
    <div class="headline headline--hero">3X YOUR SALES</div>
    <div class="headline headline--offer">Offering free smart devices</div>
    <div class="headline headline--bonus">As a bonus for buying your</div>
    <div class="headline headline--product">Product or service</div>

    <svg class="decor" viewBox="0 0 716 716" aria-hidden="true">
      <g fill="#ffffff">
        <circle cx="627" cy="27" r="2.5"/><circle cx="637" cy="27" r="2.5"/><circle cx="647" cy="27" r="2.5"/><circle cx="657" cy="27" r="2.5"/><circle cx="667" cy="27" r="2.5"/><circle cx="677" cy="27" r="2.5"/><circle cx="687" cy="27" r="2.5"/>
        <circle cx="624" cy="38" r="2.5"/><circle cx="634" cy="38" r="2.5"/><circle cx="644" cy="38" r="2.5"/><circle cx="654" cy="38" r="2.5"/><circle cx="664" cy="38" r="2.5"/><circle cx="674" cy="38" r="2.5"/>
      </g>
      <g fill="#ff7f00">
        <circle cx="39" cy="57" r="2.3"/><circle cx="39" cy="69" r="2.3"/><circle cx="39" cy="81" r="2.3"/><circle cx="39" cy="93" r="2.3"/><circle cx="39" cy="105" r="2.3"/>
        <circle cx="50" cy="66" r="2.3"/><circle cx="50" cy="78" r="2.3"/><circle cx="50" cy="90" r="2.3"/><circle cx="50" cy="102" r="2.3"/>
      </g>
      <g stroke-width="3" stroke-linecap="round">
        <path d="M613 262v16M605 270h16" stroke="#ff7f00"/>
        <path d="M79 319v16M71 327h16" stroke="#ffffff"/>
        <path d="M662 544v16M654 552h16" stroke="#ffffff"/>
        <path d="M142 579v16M134 587h16" stroke="#ff7f00"/>
      </g>
    </svg>

    <div class="footer-band">
      <div class="brand"><span class="brand-dot"></span>BRIGHTLANE PROMOWORKS</div>
      <div class="cta">START A RISK FREE TRIAL</div>
    </div>
  </div>
</div>

</body>
</html>
```